Futuristic but clean CD Cover Design

I need a CD Cover design for my next EP. The music is electronic pop. I am looking for something clean but futuristic with neon colors .Name of band: peopleASponiesName of Album: CeylonI have attached my logo.I have also attached CD covers of the color scheme and clean look I am looking for.Thanks

Industry/Entity Type

Film Production

Requirements
Must have
• A clean future look. The music is electronic pop.

```html
<!DOCTYPE html>
<html lang="en">
<head>
<meta charset="utf-8">
<title>Mirvane — kettlesINorbit</title>
<link rel="stylesheet" href="https://fonts.googleapis.com/css2?family=Bodoni+Moda:opsz,wght@6..96,500&display=swap">
<style>
  :root {
    --stage: #e1e1e1;
    --sleeve: #030205;
    --ink: #ffffff;
    --glow-gold: #ffd37a;
    --glow-amber: #f5a13a;
    --glow-red: #d8231c;
    --glow-green: #6ef08a;
    --glow-violet: #3a1f4a;
    --glow-wine: #5a1428;
  }
  * { margin: 0; padding: 0; box-sizing: border-box; }
  html, body {
    width: 1200px;
    height: 1040px;
    overflow: hidden;
    background: var(--stage);
  }
  .cover {
    position: absolute;
    left: 120px;
    top: 40px;
    width: 960px;
    height: 960px;
    background: var(--sleeve);
    overflow: hidden;
    font-family: "Bodoni Moda", "Didot", serif;
    color: var(--ink);
  }
  .cover__artwork {
    position: absolute;
    inset: 0;
    background:
      radial-gradient(ellipse 22% 20% at 72% 55%, rgba(110,240,138,0.85), rgba(110,240,138,0) 100%),
      radial-gradient(ellipse 26% 24% at 52% 52%, rgba(255,211,122,0.9), rgba(245,161,58,0) 100%),
      radial-gradient(ellipse 24% 30% at 46% 66%, rgba(216,35,28,0.85), rgba(216,35,28,0) 100%),
      radial-gradient(ellipse 30% 34% at 68% 78%, rgba(245,161,58,0.55), rgba(245,161,58,0) 100%),
      radial-gradient(ellipse 45% 55% at 70% 55%, rgba(90,20,40,0.9), rgba(58,31,74,0.35) 70%, rgba(3,2,5,0) 100%),
      radial-gradient(ellipse 40% 25% at 85% 8%, rgba(110,240,138,0.25), rgba(3,2,5,0) 100%);
  }
  .cover__band {
    position: absolute;
    left: 72px;
    top: 300px;
    display: flex;
    align-items: center;
    gap: 12px;
    font-size: 30px;
    font-weight: 500;
    letter-spacing: 0.01em;
    color: var(--ink);
  }
  .cover__band-mark {
    width: 14px;
    height: 14px;
    background: var(--ink);
  }
  .cover__title {
    position: absolute;
    left: 100px;
    top: 752px;
    font-size: 82px;
    font-weight: 500;
    line-height: 1;
    letter-spacing: 0.01em;
    color: var(--ink);
  }
</style>
</head>
<body>
  <main class="cover">
    <div class="cover__artwork" role="img" aria-label="Glowing abstract fractal rings in neon red, gold and green on black"></div>
    <div class="cover__band">
      <span class="cover__band-mark"></span>
      <span class="cover__band-name">kettlesINorbit</span>
    </div>
    <h1 class="cover__title">Mirvane</h1>
  </main>
</body>
</html>
```